DENTIST OFFICE POST CARD DESIGN

COMPANY NAME: BEARABLE DENTISTRYCome and see if Meridale Dentistry is for you.... ALWAYSWELCOMINGNEW PATIENTS!Call today for your appointment!607 918 2763 We are located on 14 Palvin Street , Oneonta, Ny----(map scketch)All in one stop for all your dental care needsCOSMETIC DENTISTRYDENTAL IMPLANTSROOT CANALSVENEERSWHITENINGSFILLINGSCROWNSBRIDGESDENTURESEXTRACTIONSGUM TREATMENTSSNAP ON SMILECOLOR------ANYPOSTCARD INDICIA;PRSRT STDECRWSSU.S. POSTAGEPAIDEDDM RETAILLocalPostal Customer

```html
<!DOCTYPE html>
<html lang="en">
<head>
<meta charset="utf-8">
<title>Meridale Dentistry Postcard</title>
<link rel="stylesheet" href="https://fonts.googleapis.com/css2?family=Bebas+Neue&display=swap">
<style>
  :root {
    --teal: #5cc5c4;
    --teal-light: #7fd3d2;
    --map-line: #a9e2e0;
    --navy: #2b4d6e;
    --pin-fill: #8b9bb4;
    --white: #ffffff;
    --paper: #ffffff;
  }
  * { margin: 0; padding: 0; box-sizing: border-box; }
  html, body {
    width: 1200px; height: 378px; overflow: hidden;
    background: var(--paper);
    font-family: "Bebas Neue", "Arial Narrow", sans-serif;
  }
  .postcard { position: relative; width: 1200px; height: 378px; }
  .side {
    position: absolute; top: 0; height: 372px;
    background: var(--teal); overflow: hidden;
  }
  .side--front { left: 0; width: 585px; }
  .side--back { left: 615px; width: 585px; }

  .front-title {
    position: absolute; top: 56px; left: 0; width: 100%;
    text-align: center; color: var(--white);
    font-size: 27px; letter-spacing: 0.5px;
  }
  .mascot {
    position: absolute; left: 205px; top: 118px; width: 185px; height: 170px;
    border-radius: 40% 40% 30% 30%;
    background: radial-gradient(circle at 50% 45%, #f4fbfb 0%, #d8f0f0 55%, var(--teal) 75%);
  }
  .front-tagline {
    position: absolute; top: 303px; left: 0; width: 100%;
    text-align: center; color: var(--navy); font-size: 14.5px; letter-spacing: 0.3px;
  }

  .map {
    position: absolute; right: 0; top: 0; width: 330px; height: 100%;
    background: linear-gradient(90deg, var(--teal) 0%, var(--teal-light) 40%, var(--map-line) 100%);
    opacity: 0.8;
  }
  .back-text {
    position: absolute; left: 20px; top: 17px;
    font-size: 15px; line-height: 17.5px; letter-spacing: 0.3px;
  }
  .back-text .lead { color: var(--white); }
  .back-text .services-heading { color: var(--white); margin-top: 35px; }
  .back-text .services { color: var(--navy); list-style: none; font-size: 15.5px; }
  .back-text .services li { line-height: 17.4px; }

  .mini-mascot {
    position: absolute; left: 160px; top: 292px; width: 80px; height: 62px;
    border-radius: 40%;
    background: radial-gradient(circle at 45% 50%, #f4fbfb 0%, #cdeceb 55%, var(--teal) 80%);
  }
  .location-pin { position: absolute; left: 404px; top: 20px; }
</style>
</head>
<body>
<main class="postcard">
  <section class="side side--front">
    <h1 class="front-title">MERIDALE DENTISTRY</h1>
    <div class="mascot" role="img" aria-label="Illustration of a smiling cartoon tooth holding a toothbrush and toothpaste, surrounded by bubbles"></div>
    <p class="front-tagline">COME AND SEE IF MERIDALE DENTISTRY IS FOR YOU</p>
  </section>

  <section class="side side--back">
    <div class="map" role="img" aria-label="Sketch map of the streets around the office"></div>
    <div class="back-text">
      <p class="lead">ALWAYS WELCOMING NEW PATIENTS!</p>
      <p class="lead">CALL TODAY FOR YOUR APPOINTMENT! 607 918 2763</p>
      <p class="lead">WE ARE LOCATED ON 14 PALVIN STREET , ONEONTA, NY</p>
      <p class="services-heading">ALL IN ONE STOP FOR ALL YOUR DENTAL CARE</p>
      <ul class="services">
        <li>NEED SCOSMETIC DENTISTRYDENTAL</li>
        <li>IMPLANTSROOT</li>
        <li>CANALSVENEERS</li>
        <li>WHITENINGS FILLINGS</li>
        <li>CROWNS BRIDGES</li>
        <li>DENTURESEXTRACTIONS</li>
        <li>GUM TREATMENTSCLIP</li>
        <li>FIT GRINCOLOR</li>
      </ul>
    </div>
    <div class="mini-mascot" role="img" aria-label="Small illustration of the cartoon tooth with toothbrush"></div>
    <svg class="location-pin" width="140" height="245" viewBox="0 0 140 245" aria-label="Map pin marking Meridale Dentistry">
      <path d="M58 128 L70 240 L82 128 Z" fill="var(--navy)"/>
      <circle cx="70" cy="70" r="64" fill="var(--navy)"/>
      <circle cx="70" cy="70" r="55" fill="var(--pin-fill)"/>
      <text x="70" y="66" text-anchor="middle" font-family="Bebas Neue, Arial Narrow, sans-serif" font-size="16" fill="var(--navy)">MERIDALE</text>
      <text x="70" y="84" text-anchor="middle" font-family="Bebas Neue, Arial Narrow, sans-serif" font-size="16" fill="var(--navy)">DENTISTRY</text>
    </svg>
  </section>
</main>
</body>
</html>
```